Commercial/Retail/Office Real Estate Lease Brochure for Vacant Space

We need a commercial Real Estate Fyler Template for lease space. We would like it for Vacant lease spaces and new buildings in the commercial, retail, office and industrial lease space. The flyer should have sections for: Highlights (site size, leasable area, Location, Ammenties etc.), concept floor plan or site plan, contact information, project/construction description.

Target Market(s)

Commercial Leasing for Offices and Retail Space

Industry/Entity Type

Real Estate Leasing and Development

Requirements
Must have
• Clean, timeless not overly busy template with spots for key metrics (square feet leaseable space, parking etc), location for pictures
Nice to have
• Lorvex Crane Real Estate Logo for header/foot, reusable with adjustments for other spaces
Should not have
• Busy, overall colorfull or contrasting

```html
<!DOCTYPE html>
<html lang="en">
<head>
<meta charset="utf-8">
<title>Lorvex Crane Real Estate – Lease Brochure</title>
<link rel="stylesheet" href="https://fonts.googleapis.com/css2?family=Arimo:ital,wght@0,400;0,700;1,700&family=Libre+Baskerville:wght@700&display=swap">
<style>
  :root {
    --board: #c4c4c4;
    --paper: #ffffff;
    --tan: #c2b89f;
    --heading: #6f6454;
    --ink: #2e2e2e;
    --muted: #4a4a4a;
    --photo-evening: linear-gradient(135deg, #34405f 0%, #262a36 100%);
    --photo-daylight: linear-gradient(135deg, #93a9bf 0%, #8c7c6a 100%);
    --plan-fill: linear-gradient(135deg, #d9d9d9 0%, #ededed 100%);
  }
  * { margin: 0; padding: 0; box-sizing: border-box; }
  html, body { width: 1200px; height: 1200px; overflow: hidden; background: var(--board); }
  body { position: relative; font-family: "Arimo", Arial, sans-serif; color: var(--ink); }

  .spread { position: absolute; background: var(--paper); box-shadow: 2px 3px 6px rgba(0,0,0,.28); overflow: hidden; }
  .cover { left: 196px; top: 55px; width: 656px; height: 425px; }
  .spread-a { left: 488px; top: 504px; width: 486px; height: 314px; }
  .spread-b { left: 366px; top: 842px; width: 486px; height: 314px; }

  .band, .photo, .plan, .text, .heading, .brand, .page-num, .contact, .quote, .rule { position: absolute; }
  .band { background: var(--tan); }
  .photo { display: block; }
  .photo--evening { background: var(--photo-evening); }
  .photo--daylight { background: var(--photo-daylight); }
  .plan { background: var(--plan-fill); border: 1px solid #c8c8c8; }

  .brand { color: #2f2f2f; font-weight: 400; letter-spacing: .08em; line-height: 1.2; text-align: right; }
  .brand__mark { display: inline-block; width: 8px; height: 8px; background: #2f2f2f; margin-right: 5px; vertical-align: middle; }

  .heading { font-family: "Libre Baskerville", Georgia, serif; font-weight: 700; color: var(--heading); text-transform: uppercase; line-height: 1.22; font-size: 11px; white-space: nowrap; }
  .cover-title { left: 367px; top: 332px; font-size: 16.5px; }
  .cover-sub { position: absolute; left: 367px; top: 358px; font-size: 9.4px; color: var(--muted); white-space: nowrap; }
  .cover-foot { position: absolute; right: 29px; top: 397px; font-size: 5.6px; line-height: 8.6px; text-align: right; }

  .contact { left: 47px; top: 324px; }
  .contact__title { font-size: 7.4px; font-weight: 700; color: var(--heading); letter-spacing: .02em; }
  .contact__list { list-style: none; margin: 7px 0 0 8px; font-size: 5.6px; line-height: 9.7px; color: var(--muted); }

  .text { font-size: 4.2px; line-height: 5.6px; color: var(--ink); }
  .text p + p { margin-top: 5.6px; }
  .quote { font-size: 6.9px; line-height: 9.6px; font-style: italic; font-weight: 700; color: var(--heading); }
  .rule { height: 3px; background: var(--tan); }
  .page-num { font-size: 4.2px; color: var(--ink); }
</style>
</head>
<body>

  <section class="spread cover">
    <div class="band" style="left:627px; top:0; width:16px; height:164px;"></div>

    <div class="brand" style="right:135px; top:86px; font-size:10.5px;">
      <span class="brand__mark"></span>LORVEX CRANE<br>REAL ESTATE
    </div>

    <div class="band" style="left:366px; top:142px; width:155px; height:22px;"></div>
    <div class="photo photo--evening" role="img" aria-label="Photograph of the two-storey office building at dusk" style="left:328px; top:164px; width:299px; height:145px;"></div>
    <div class="band" style="left:366px; top:309px; width:155px; height:17px;"></div>

    <h1 class="heading cover-title">Project Description</h1>
    <p class="cover-sub">Lorem ipsum dolor sit amet, consectetur adipiscing elit</p>
    <p class="cover-foot">Lorem ipsum dolor sit amet<br>Lorem ipsum dolor sit amet</p>

    <div class="brand" style="left:47px; top:248px; font-size:8.6px;">
      <span class="brand__mark"></span>LORVEX CRANE<br>REAL ESTATE
    </div>
    <div class="band" style="left:0; top:290px; width:174px; height:19px;"></div>

    <div class="contact">
      <h2 class="contact__title">CONTACT US</h2>
      <ul class="contact__list">
        <li>Lorem ipsum dolor sit amet</li>
        <li>Lorem ipsum dolor sit amet</li>
        <li>Lorem ipsum dolor sit amet</li>
      </ul>
    </div>
  </section>

  <section class="spread spread-a">
    <div class="band" style="left:364px; top:0; width:122px; height:14px;"></div>

    <h2 class="heading" style="left:43px; top:35px;">Project<br>Description</h2>
    <div class="band" style="left:43px; top:74px; width:151px; height:14px;"></div>
    <div class="photo photo--daylight" role="img" aria-label="Architectural rendering of the brick office building with parking" style="left:29px; top:88px; width:214px; height:115px;"></div>
    <div class="text" style="left:43px; top:224px; width:151px;">
      <p>Lorem ipsum dolor sit amet, consectetur adipiscing elit, sed do eiusmod tempor incididunt ut labore et dolore magna aliqua. Ut enim ad minim veniam, quis nostrud exercitation ullamco laboris nisi ut aliquip ex ea commodo consequat. Duis aute irure dolor in reprehenderit in voluptate velit esse cillum dolore eu fugiat nulla pariatur. Excepteur sint occaecat cupidatat non proident, sunt in culpa qui officia deserunt mollit anim id est laborum.</p>
      <p>Lorem ipsum dolor sit amet, consectetur adipiscing elit, sed do eiusmod tempor incididunt ut labore et dolore magna aliqua. Ut enim ad minim veniam, quis nostrud exercitation ullamco laboris nisi ut aliquip ex ea commodo consequat. Duis aute irure dolor in reprehenderit in voluptate velit esse cillum dolore eu fugiat nulla pariatur. Excepteur sint occaecat cupidatat non proident, sunt in culpa qui officia deserunt mollit anim id est laborum.</p>
    </div>
    <span class="page-num" style="left:20px; top:301px;">1</span>

    <div class="band" style="left:243px; top:203px; width:35px; height:111px;"></div>

    <h2 class="heading" style="left:279px; top:35px;">Project<br>Details</h2>
    <div class="text" style="left:279px; top:74px; width:88px;">
      <p>Lorem ipsum dolor sit amet, consectetur adipiscing elit, sed do eiusmod tempor incididunt ut labore et dolore magna aliqua. Ut enim ad minim veniam, quis nostrud exercitation ullamco laboris nisi ut aliquip ex ea commodo consequat. Duis aute irure dolor in reprehenderit in voluptate velit esse cillum dolore eu fugiat nulla pariatur. Excepteur sint occaecat cupidatat non proident, sunt in culpa qui officia deserunt mollit anim id est laborum.</p>
    </div>
    <div class="text" style="left:379px; top:74px; width:88px;">
      <p>Lorem ipsum dolor sit amet, consectetur adipiscing elit, sed do eiusmod tempor incididunt ut labore et dolore magna aliqua. Ut enim ad minim veniam, quis nostrud exercitation ullamco laboris nisi ut aliquip ex ea commodo consequat. Duis aute irure dolor in reprehenderit in voluptate velit esse cillum dolore eu fugiat nulla pariatur. Excepteur sint occaecat cupidatat non proident, sunt in culpa qui officia deserunt mollit anim id est laborum.</p>
    </div>
    <div class="photo photo--daylight" role="img" aria-label="Architectural rendering of the building corner with glass entrance and landscaping" style="left:278px; top:155px; width:208px; height:135px;"></div>
    <span class="page-num" style="left:465px; top:301px;">2</span>
  </section>

  <section class="spread spread-b">
    <div class="band" style="left:15px; top:0; width:11px; height:200px;"></div>

    <h2 class="heading" style="left:43px; top:36px;">Project<br>Highlights</h2>
    <div class="text" style="left:43px; top:73px; width:112px;">
      <p>Lorem ipsum dolor sit amet, consectetur adipiscing elit, sed do eiusmod tempor incididunt ut labore et dolore magna aliqua. Ut enim ad minim veniam, quis nostrud exercitation ullamco laboris nisi ut aliquip ex ea commodo consequat. Duis aute irure dolor in reprehenderit in voluptate velit esse cillum dolore eu fugiat nulla pariatur. Excepteur sint occaecat cupidatat non proident, sunt in culpa qui officia deserunt mollit anim id est laborum.</p>
      <p>Lorem ipsum dolor sit amet, consectetur adipiscing elit, sed do eiusmod tempor incididunt ut labore et dolore magna aliqua. Ut enim ad minim veniam, quis nostrud exercitation ullamco laboris nisi ut aliquip ex ea commodo consequat. Duis aute irure dolor in reprehenderit in voluptate velit esse cillum dolore eu fugiat nulla pariatur. Excepteur sint occaecat cupidatat non proident, sunt in culpa qui officia deserunt mollit anim id est laborum.</p>
    </div>

    <p class="quote" style="left:166px; top:72px; width:62px;">Lorem ipsum dolor sit amet, consectetur adipiscing elit, sed do eiusmod tempor incididunt ut labore et dolore magna aliqua. consequat.</p>
    <div class="rule" style="left:166px; top:179px; width:60px;"></div>

    <div class="photo photo--daylight" role="img" aria-label="Photograph of the completed brick office building and parking lot" style="left:26px; top:200px; width:129px; height:79px;"></div>
    <div class="text" style="left:166px; top:230px; width:60px;">
      <p>Lorem ipsum dolor sit amet, consectetur adipiscing elit, sed do eiusmod tempor incididunt ut labore et dolore magna aliqua. Ut enim ad minim veniam, quis nostrud exercitation ullamco laboris nisi ut aliquip ex ea commodo consequat.</p>
    </div>
    <span class="page-num" style="left:20px; top:301px;">3</span>

    <h2 class="heading" style="left:279px; top:36px;">Project Image Plan</h2>
    <div class="plan" role="img" aria-label="Concept floor plan of the leasable office space" style="left:283px; top:65px; width:174px; height:118px;"></div>

    <div class="band" style="left:314px; top:200px; width:172px; height:17px;"></div>
    <div class="text" style="left:314px; top:227px; width:125px;">
      <p>Lorem ipsum dolor sit amet, consectetur adipiscing elit, sed do eiusmod tempor incididunt ut labore et dolore magna aliqua. Ut enim ad minim veniam, quis nostrud exercitation ullamco laboris nisi ut aliquip ex ea commodo consequat.</p>
      <p>Lorem ipsum dolor sit amet, consectetur adipiscing elit, sed do eiusmod tempor incididunt ut labore et dolore magna aliqua. Ut enim ad minim veniam, quis nostrud exercitation ullamco laboris nisi ut aliquip ex ea commodo consequat.</p>
    </div>
    <span class="page-num" style="left:465px; top:301px;">4</span>
  </section>

</body>
</html>
```